Event Website Design

We need a new website design for an events driven website. The domain for this site is http://brackmoorhalls.co.uk. The site is up and running but needs a new fresh, modern look.
I've attached a Balamiq Mockup for the layout of the home page. Also attached is a png of the logo.
Key colours for the site are 0f7e6a, 35bde, d57835 & 373737.
Font to use is Proxima Nova
Width of the site should be 1200px
The design should be contemporary with minimal clutter.
Websites to references are…
http://vantora.london/
http://www.thekrd.co.uk/
These are just guidelines, please feel free to use you own creative judgment.
The selected design file needs to be supplied as an editable PSD.
Updates
Reason: I've submitted 5 designs to the client, who will select the one they want. I will then choose that design. So please be patient as I'm waiting for a decision from my client.
Industry/Entity Type
Events
Number of Pages Required
1 page
Look and feel
Each slider illustrates characteristics of the customer's brand and the style your logo design should communicate.

```html
<!DOCTYPE html>
<html lang="en">
<head>
<meta charset="utf-8">
<title>Brackmoor Halls – Entertainment &amp; Sporting Centre</title>
<link href="https://fonts.googleapis.com/css2?family=Montserrat:wght@400;500;600;700;800&display=swap" rel="stylesheet">
<style>
:root{
  --teal:#1fa58b;
  --teal-dark:#0f7e6a;
  --cyan:#2bb7e0;
  --blue:#2f95bf;
  --orange:#d57835;
  --charcoal:#373737;
  --header-bg:#2a2b2d;
  --dark:#232323;
  --dark-card:#1b1b1b;
  --footer-bg:#2d2e30;
  --light:#e9ecee;
  --white:#ffffff;
  --muted:#9a9a9a;
}
*{box-sizing:border-box;margin:0;padding:0}
html,body{width:1200px;height:3403px;overflow:hidden}
body{font-family:"Montserrat",Arial,sans-serif;color:var(--white);background:var(--white);position:relative}
.abs{position:absolute}
a{color:inherit;text-decoration:none}

/* Header */
.site-header{position:absolute;left:0;top:0;width:1200px;height:177px;background:var(--header-bg)}
.brand{position:absolute;left:48px;top:40px;display:flex;align-items:center;gap:14px}
.brand-mark{width:34px;height:34px;background:var(--teal)}
.brand-name{font-size:34px;font-weight:800;letter-spacing:1px;color:var(--white);white-space:nowrap}
.tagline{position:absolute;left:48px;top:136px;font-size:12px;font-weight:700;color:var(--white)}
.util-links{position:absolute;right:58px;top:24px;display:flex;gap:10px;font-size:12px;color:#a9a9a9}
.util-links span.sep{color:var(--teal)}
.search{position:absolute;left:685px;top:61px;width:460px;height:41px;border-radius:21px;background:#f1f1f1;color:#9b9b9b;font-size:14px;padding:11px 22px}
.search svg{position:absolute;right:16px;top:11px}
.box-office{position:absolute;left:686px;top:122px;font-size:21px;font-weight:700;color:var(--teal);white-space:nowrap;line-height:30px}
.box-office b{color:var(--white);font-weight:700}
.social-sq{position:absolute;top:116px;width:38px;height:38px;border:2px solid #cfcfcf;display:flex;align-items:center;justify-content:center}

/* Nav */
.main-nav{position:absolute;left:0;top:177px;width:1200px;height:73px;background:var(--teal);display:flex;justify-content:space-between;padding:0 36px}
.main-nav a{font-size:13px;font-weight:700;line-height:73px;padding:0 4px;white-space:nowrap}
.main-nav a.active{background:#2fb89e;padding:0 14px;border-bottom:3px solid #fff}

/* Hero */
.hero{position:absolute;left:0;top:250px;width:1200px;height:571px;background:linear-gradient(180deg,#2b3033 0%,#4a5155 30%,#33393d 55%,#5a6166 80%,#3a3f43 100%)}
.hero-panel{position:absolute;left:218px;top:120px;width:762px;height:333px;background:rgba(30,30,30,.72);text-align:center}
.hero-title{font-size:70px;font-weight:700;margin-top:30px;line-height:1}
.hero-title .c1{color:var(--cyan)}.hero-title .c2{color:var(--teal)}
.hero-date{font-size:44px;font-weight:700;margin-top:6px}
.hero-text{font-size:15px;line-height:27px;margin-top:18px}
.btn-outline{display:inline-block;border:2px solid #fff;font-size:13px;font-weight:700;padding:10px 0;width:127px;text-align:center;letter-spacing:1px}
.hero-btns{margin-top:18px;display:flex;justify-content:center;gap:12px}
.hero-btns .teal{color:var(--teal)}.hero-btns .orange{color:var(--orange)}
.dots-v{position:absolute;right:16px;top:410px;display:flex;flex-direction:column;gap:6px}
.dots-v i{width:8px;height:8px;border-radius:50%;background:#ddd;display:block}

/* Events slider */
.events{position:absolute;left:0;top:821px;width:1200px;height:540px;background:var(--light)}
.notch{position:absolute;left:560px;top:0}
.slider-arrow{position:absolute;top:49px;width:32px;height:32px;border-radius:50%;background:var(--teal)}
.event-card{position:absolute;top:98px;width:245px;height:392px;background:#333}
.event-card .photo{position:absolute;inset:0}
.event-card .body{position:absolute;left:18px;right:14px;top:238px}
.event-card h3{font-size:25px;font-weight:700;line-height:1;white-space:nowrap}
.event-card .date{font-size:15px;font-weight:700;margin-top:8px}
.event-card p{font-size:10px;line-height:15px;margin-top:8px}
.mini-btns{display:flex;gap:8px;margin-top:26px}
.mini-btn{border:1px solid var(--teal);color:var(--teal);font-size:9px;font-weight:700;width:70px;text-align:center;padding:6px 0}

/* News */
.news{position:absolute;left:0;top:1361px;width:1200px;height:608px;background:var(--dark)}
.news h2{position:absolute;left:0;width:1200px;top:68px;text-align:center;font-size:28px;font-weight:700}
.news .rule{position:absolute;left:571px;top:114px;width:58px;height:3px;background:var(--teal)}
.news-item{position:absolute;top:165px;height:272px;background:var(--dark-card)}
.news-item .photo{position:absolute;left:0;top:0;width:268px;height:272px}
.news-item .frame{position:absolute;left:14px;top:14px;width:254px;height:244px;border:2px solid var(--orange);border-right:none}
.news-item .text{position:absolute;left:292px;top:32px;width:230px}
.news-item h3{font-size:15px;font-weight:700}
.meta{font-size:11px;margin-top:10px;display:flex;gap:8px;align-items:center;color:#ddd;white-space:nowrap}
.meta svg{flex:none}
.news-item p{font-size:11.5px;line-height:18px;margin-top:26px;color:#ddd}
.news-item .line{position:absolute;left:268px;top:246px;width:122px;height:2px;background:var(--orange)}
.news-item .more{position:absolute;left:390px;top:230px;width:110px;height:30px;border:2px solid var(--orange);font-size:12px;font-weight:600;text-align:center;line-height:26px;letter-spacing:1px}
.dots-h{position:absolute;left:577px;top:465px;display:flex;gap:5px}
.dots-h i{width:9px;height:9px;border-radius:50%;background:#fff;display:block}
.dots-h i.on{background:#777}
.see-all{position:absolute;left:506px;top:506px;width:195px;height:46px;border:3px solid var(--orange);border-radius:23px;font-size:15px;font-weight:700;text-align:center;line-height:40px}
.corner{position:absolute;top:0}

/* Features */
.features{position:absolute;left:0;top:1969px;width:1200px;height:492px;background:linear-gradient(180deg,#fff,#f1f1f1)}
.feature{position:absolute;top:68px;width:307px;height:358px;background:#222}
.feature header{height:100px;background:var(--blue);display:flex;align-items:center;justify-content:center;text-align:center;font-size:23px;font-weight:700;line-height:27px}
.feature .photo{position:absolute;left:0;top:100px;width:307px;height:258px}
.feature .icon{position:absolute;left:103px;top:118px}
.feature .read{position:absolute;left:96px;top:280px;width:115px;height:34px;background:var(--blue);font-size:11px;font-weight:700;line-height:34px;padding-left:14px}
.feature .read svg{position:absolute;right:10px;top:9px}

/* Sports */
.sports{position:absolute;left:0;top:2461px;width:1200px;height:555px;background:linear-gradient(180deg,#1d78c0 0%,#3aa2dd 36%,#9fc9e4 44%,#1c4f86 46%,#1e4a78 66%,#3b4652 78%,#8a7a6a 90%,#6b5a66 100%)}
.sports h2{position:absolute;left:0;width:1200px;top:50px;text-align:center;font-size:90px;font-weight:800;line-height:1}
.sports .cta{position:absolute;left:372px;top:152px;width:426px;height:54px;border:3px solid #fff;border-radius:27px;font-size:23px;font-weight:600;text-align:center;line-height:48px}

/* Footer */
.site-footer{position:absolute;left:0;top:3016px;width:1200px;height:336px;background:var(--footer-bg)}
.col-div{position:absolute;top:0;width:1px;height:336px;background:#444}
.contact{position:absolute;left:80px;top:82px}
.contact h4{font-size:13px;font-weight:700;margin-bottom:12px}
.contact p,.links a{font-size:10.5px;color:var(--muted);line-height:24px;display:block;text-transform:uppercase}
.links{position:absolute;top:105px;width:190px}
.links a{line-height:36px}
.foot-brand{position:absolute;left:820px;top:128px;width:360px;text-align:center;font-size:26px;font-weight:800;letter-spacing:1px;white-space:nowrap}
.foot-brand i{display:inline-block;width:20px;height:20px;background:var(--teal);vertical-align:-2px;margin-right:10px}
.soc{position:absolute;top:223px;width:50px;height:50px;border-radius:50%;background:#3d3e40}
.soc.red{background:#e8403a}
.copyright{position:absolute;left:0;top:3352px;width:1200px;height:51px;background:#fafafa;color:#777;font-size:10px;text-align:center;line-height:51px;letter-spacing:.5px}
</style>
</head>
<body>

<header class="site-header">
  <div class="brand"><span class="brand-mark"></span><span class="brand-name">BRACKMOOR HALLS</span></div>
  <div class="tagline">Somerset's Premier Entertainment &amp; Sporting Centre</div>
  <nav class="util-links">
    <a href="#">Gift Voucher</a><span class="sep">•</span>
    <a href="#">Join Our Mailing List</a><span class="sep">•</span>
    <a href="#">My Account</a><span class="sep">•</span>
    <a href="#">Basket</a><span class="sep">•</span>
    <a href="#">Register</a>
  </nav>
  <div class="search">Search
    <svg width="18" height="18" viewBox="0 0 18 18" fill="none" stroke="#888" stroke-width="2"><circle cx="7.5" cy="7.5" r="5.5"/><path d="M12 12l5 5"/></svg>
  </div>
  <div class="box-office">Box Office: <b>01632 960 450</b></div>
  <span class="social-sq" style="left:1015px" aria-label="Social link"></span>
  <span class="social-sq" style="left:1061px" aria-label="Social link"></span>
  <span class="social-sq" style="left:1107px" aria-label="Calendar"><svg width="20" height="20" viewBox="0 0 20 20" fill="none" stroke="#fff" stroke-width="1.6"><rect x="2" y="4" width="16" height="14"/><path d="M2 8h16M6 2v4M14 2v4M6 11h2M10 11h2M14 11h0M6 14h2M10 14h2"/></svg></span>
</header>

<nav class="main-nav">
  <a class="active" href="#">WHAT'S ON</a>
  <a href="#">CONFERENCING &amp; EVENTS</a>
  <a href="#">SPORTS &amp; LEISURE</a>
  <a href="#">LANTERN THEATRE</a>
  <a href="#">PLAN YOUR VISIT</a>
  <a href="#">NEWS</a>
  <a href="#">DISCOVER MORE</a>
  <a href="#">CONTACT US</a>
</nav>

<section class="hero" role="img" aria-label="Swimmer in open water at dusk">
  <div class="hero-panel">
    <h1 class="hero-title"><span class="c1">SHOW</span> <span class="c2">TITTLE</span></h1>
    <div class="hero-date">DATE: 07 JAN 2017</div>
    <p class="hero-text">Lorem Ipsum is simply dummy text of the printing and typesetting industry.<br>Lorem Ipsum has been the industry's standard dummy text ever since the 1500s</p>
    <div class="hero-btns"><a class="btn-outline teal" href="#">READ MORE</a><a class="btn-outline orange" href="#">BOOK NOW</a></div>
  </div>
  <div class="dots-v"><i></i><i></i><i></i></div>
</section>

<section class="events">
  <svg class="notch" width="80" height="28" viewBox="0 0 80 28"><path d="M0 0h80L40 28z" fill="#2e3337"/><path d="M32 6l8 7 8-7" stroke="#fff" stroke-width="2.5" fill="none"/></svg>
  <span class="slider-arrow" style="left:1025px"><svg width="32" height="32"><path d="M18 10l-6 6 6 6" stroke="#fff" stroke-width="2.5" fill="none"/></svg></span>
  <span class="slider-arrow" style="left:1082px"><svg width="32" height="32"><path d="M14 10l6 6-6 6" stroke="#fff" stroke-width="2.5" fill="none"/></svg></span>

  <article class="event-card" style="left:86px">
    <div class="photo" role="img" aria-label="Tennis ball on racket strings" style="background:linear-gradient(180deg,#3f5a4e,#6d7a52 45%,#1b1b1b 75%)"></div>
    <div class="body"><h3>SHOW TITTLE</h3><div class="date">Date: 07 jan 2017</div><p>Lorem Ipsum is simply dummy text of the printing and typesetting industry.</p><div class="mini-btns"><span class="mini-btn">READ MORE</span><span class="mini-btn">BOOK NOW</span></div></div>
  </article>
  <article class="event-card" style="left:347px">
    <div class="photo" role="img" aria-label="Guitarist playing on stage" style="background:linear-gradient(180deg,#2c4f7a,#6a6e76 45%,#1b1b1b 75%)"></div>
    <div class="body"><h3>SHOW TITTLE</h3><div class="date">Date: 07 jan 2017</div><p>Lorem Ipsum is simply dummy text of the printing and typesetting industry.</p><div class="mini-btns"><span class="mini-btn">READ MORE</span><span class="mini-btn">BOOK NOW</span></div></div>
  </article>
  <article class="event-card" style="left:608px">
    <div class="photo" role="img" aria-label="Track cyclist racing" style="background:linear-gradient(180deg,#4a6a3a,#7d5a3e 45%,#1b1b1b 75%)"></div>
    <div class="body"><h3>SHOW TITTLE</h3><div class="date">Date: 07 jan 2017</div><p>Lorem Ipsum is simply dummy text of the printing and typesetting industry.</p><div class="mini-btns"><span class="mini-btn">READ MORE</span><span class="mini-btn">BOOK NOW</span></div></div>
  </article>
  <article class="event-card" style="left:871px">
    <div class="photo" role="img" aria-label="Performer under blue stage lights" style="background:linear-gradient(180deg,#1f3ea0,#2a2f80 45%,#14142a 75%)"></div>
    <div class="body"><h3>SHOW TITTLE</h3><div class="date">Date: 07 jan 2017</div><p>Lorem Ipsum is simply dummy text of the printing and typesetting industry.</p><div class="mini-btns"><span class="mini-btn">READ MORE</span><span class="mini-btn">BOOK NOW</span></div></div>
  </article>
</section>

<section class="news">
  <svg class="corner" style="left:0" width="110" height="52"><path d="M0 0h110L0 52z" fill="var(--teal)"/></svg>
  <svg class="corner" style="right:0" width="110" height="52"><path d="M0 0h110v52z" fill="var(--teal)"/></svg>
  <h2>LATEST FROM BRACKMOOR HALLS</h2>
  <span class="rule"></span>

  <article class="news-item" style="left:52px;width:542px">
    <div class="photo" role="img" aria-label="Close-up of hands on a guitar in warm stage light" style="background:linear-gradient(135deg,#6b2f8a,#c23f7a 50%,#e0692f)"></div>
    <span class="frame"></span><span class="line"></span>
    <div class="text"><h3>NEWS STORY 1</h3>
      <div class="meta">
        <svg width="11" height="11" viewBox="0 0 12 12" fill="#fff"><rect x="0" y="2" width="12" height="10"/><rect x="1.5" y="5" width="9" height="5.5" fill="#1b1b1b"/></svg><span>05 October, 2016</span>
        <svg width="11" height="11" viewBox="0 0 12 12" fill="#fff" style="margin-left:8px"><circle cx="6" cy="3.5" r="3"/><path d="M0 12c0-4 3-5.5 6-5.5s6 1.5 6 5.5z"/></svg><span>Jane Ellis</span>
      </div>
      <p>Lorem Ipsum is simply dummy text of the printing and typesetting industry. Lorem Ipsum has been the industry's standard dummy text ever since the 1500s.</p></div>
    <a class="more" href="#">READ MORE</a>
  </article>
  <article class="news-item" style="left:612px;width:536px">
    <div class="photo" role="img" aria-label="Rowers on a lake at sunset" style="background:linear-gradient(180deg,#d98a2a,#b8651e 50%,#3a2a18)"></div>
    <span class="frame"></span><span class="line"></span>
    <div class="text"><h3>NEWS STORY 2</h3>
      <div class="meta">
        <svg width="11" height="11" viewBox="0 0 12 12" fill="#fff"><rect x="0" y="2" width="12" height="10"/><rect x="1.5" y="5" width="9" height="5.5" fill="#1b1b1b"/></svg><span>05 October, 2016</span>
        <svg width="11" height="11" viewBox="0 0 12 12" fill="#fff" style="margin-left:8px"><circle cx="6" cy="3.5" r="3"/><path d="M0 12c0-4 3-5.5 6-5.5s6 1.5 6 5.5z"/></svg><span>Jane Ellis</span>
      </div>
      <p>Lorem Ipsum is simply dummy text of the printing and typesetting industry. Lorem Ipsum has been the industry's standard dummy text ever since the 1500s.</p></div>
    <a class="more" href="#">READ MORE</a>
  </article>

  <div class="dots-h"><i></i><i class="on"></i><i></i><i></i></div>
  <a class="see-all" href="#">SEE ALL NEWS</a>
</section>

<section class="features">
  <article class="feature" style="left:120px">
    <header>CONFERENCES<br>&amp; EVENTS</header>
    <div class="photo" role="img" aria-label="Business people by an office window" style="background:linear-gradient(180deg,#6f6f6f,#2a2a2a)"></div>
    <svg class="icon" width="100" height="110" viewBox="0 0 100 110"><circle cx="50" cy="50" r="48" fill="rgba(215,215,215,.8)"/><path d="M40 94l10 14 10-14z" fill="rgba(215,215,215,.8)"/><rect x="28" y="54" width="44" height="16" fill="#555"/><rect x="34" y="36" width="32" height="14" fill="#555"/></svg>
    <a class="read" href="#">READ MORE<svg width="16" height="16"><circle cx="8" cy="8" r="8" fill="#fff"/><path d="M6 4l4 4-4 4" stroke="#2f95bf" stroke-width="2" fill="none"/></svg></a>
  </article>
  <article class="feature" style="left:447px">
    <header>PARTIES AT<br>BRACKMOOR HALLS</header>
    <div class="photo" role="img" aria-label="Cocktail glass on a bar" style="background:linear-gradient(180deg,#2a3f7a,#7a2a4a 60%,#1a1a2a)"></div>
    <svg class="icon" width="100" height="110" viewBox="0 0 100 110"><circle cx="50" cy="50" r="48" fill="rgba(215,215,215,.8)"/><path d="M40 94l10 14 10-14z" fill="rgba(215,215,215,.8)"/><path d="M30 30h16l-8 18zM54 30h16l-8 18z" fill="#555"/><path d="M38 48v18M62 48v18M32 66h12M56 66h12" stroke="#555" stroke-width="3"/></svg>
    <a class="read" href="#">READ MORE<svg width="16" height="16"><circle cx="8" cy="8" r="8" fill="#fff"/><path d="M6 4l4 4-4 4" stroke="#2f95bf" stroke-width="2" fill="none"/></svg></a>
  </article>
  <article class="feature" style="left:773px">
    <header>CO-WORKING<br>HUB</header>
    <div class="photo" role="img" aria-label="Hands typing on a laptop" style="background:linear-gradient(180deg,#cfcfcf,#5a5a5a)"></div>
    <svg class="icon" width="100" height="110" viewBox="0 0 100 110"><circle cx="50" cy="50" r="48" fill="rgba(215,215,215,.8)"/><path d="M40 94l10 14 10-14z" fill="rgba(215,215,215,.8)"/><circle cx="34" cy="50" r="5" fill="#555"/><circle cx="50" cy="50" r="5" fill="#555"/><circle cx="66" cy="50" r="5" fill="#555"/></svg>
    <a class="read" href="#">READ MORE<svg width="16" height="16"><circle cx="8" cy="8" r="8" fill="#fff"/><path d="M6 4l4 4-4 4" stroke="#2f95bf" stroke-width="2" fill="none"/></svg></a>
  </article>
</section>

<section class="sports" role="img" aria-label="Woman doing yoga on a clifftop overlooking the sea">
  <h2>SPORTS &amp; LEISURE</h2>
  <a class="cta" href="#">Click Here For More Information</a>
  <svg class="abs" style="left:0;bottom:0" width="100" height="50"><path d="M0 0l100 50H0z" fill="var(--blue)"/></svg>
  <svg class="abs" style="right:0;bottom:0" width="100" height="50"><path d="M100 0L0 50h100z" fill="var(--blue)"/></svg>
</section>

<footer class="site-footer">
  <div class="contact">
    <h4>CONTACT US</h4>
    <p>Brackmoor Entertainment Venue</p>
    <p>Harlow Close</p>
    <p>Brackmoor</p>
    <p>Somerset</p>
    <p>BA99 4ZZ</p>
  </div>
  <span class="col-div" style="left:345px"></span>
  <nav class="links" style="left:406px"><a href="#">What's On</a><a href="#">Conferencing &amp; Events</a><a href="#">Sports &amp; Leisure</a><a href="#">Lantern Theatre</a></nav>
  <nav class="links" style="left:621px"><a href="#">Plan Your Visit</a><a href="#">News</a><a href="#">Discover More</a><a href="#">Contact Us</a></nav>
  <span class="col-div" style="left:803px"></span>
  <div class="foot-brand"><i></i>BRACKMOOR HALLS</div>
  <span class="soc" style="left:846px" aria-label="Social link"></span>
  <span class="soc" style="left:914px" aria-label="Social link"></span>
  <span class="soc red" style="left:986px" aria-label="Video channel"></span>
  <span class="soc" style="left:1059px" aria-label="Social link"></span>
</footer>
<div class="copyright">© COPYRIGHT 2016 BRACKMOOR HALLS. ALL RIGHTS RESERVED.</div>

</body>
</html>
```